Home page concept, possible logo colour change

There is no need to code a home page, we are just looking for concept ideas.
We have had a logo designed for a new company we are starting named Corvenhall Aluminium Windows & Doors. We are manufacturing bullet resistant window frames. We have had logo designed, we like the concept of the design, but the current colours (black and red) may not be the best option, especially when designing the website home page, and how it interacts with the logo colours. I have also attached the first draft of the home page which we are not happy with. The overall design/navigation is good, we have issues with the darkened out primary image and also the amount of red on the page, it just doesn't feel right. As mentioned before we are happy to look at colour changes to the logo.
Number of Pages Required
1 page
Look and feel
Each slider illustrates characteristics of the customer's brand and the style your logo design should communicate.

```html
<!DOCTYPE html>
<html lang="en">
<head>
<meta charset="utf-8">
<title>Corvenhall Aluminium Windows &amp; Doors</title>
<link href="https://fonts.googleapis.com/css2?family=DM+Sans:wght@400;500;700&display=swap" rel="stylesheet">
<style>
  :root {
    --bg: #f5f5f5;
    --blue-deep: #0b4aa6;
    --blue-mid: #1f6fd6;
    --blue-light: #2f90f2;
    --ink: #111111;
    --body: #3a3a3a;
    --white: #ffffff;
  }
  * { margin: 0; padding: 0; box-sizing: border-box; }
  html, body { width: 1200px; height: 771px; overflow: hidden; background: var(--bg); }
  body { font-family: "DM Sans", Arial, sans-serif; }
  .page { position: relative; width: 1200px; height: 771px; overflow: hidden; background: var(--bg); }
  .backdrop { position: absolute; inset: 0; }

  .brand { position: absolute; left: 237px; top: 33px; color: var(--ink); font-weight: 700; }
  .brand-name { font-size: 27px; letter-spacing: -0.5px; line-height: 1; }
  .brand-tag { font-size: 6.5px; letter-spacing: 0.6px; text-transform: uppercase; margin-top: 2px; }

  .nav { position: absolute; top: 32px; left: 562px; display: flex; align-items: center; gap: 20px; }
  .nav a { color: var(--white); text-decoration: none; font-size: 13px; font-weight: 500; }
  .nav .enquiry { background: var(--white); color: var(--blue-deep); padding: 8px 14px; height: 31px; margin-left: 0; box-shadow: 0 6px 14px rgba(0,0,0,0.15); }

  .hero-copy { position: absolute; left: 236px; top: 230px; width: 300px; }
  .hero-title { color: var(--blue-deep); font-size: 31.5px; font-weight: 700; line-height: 1.1; letter-spacing: -0.2px; }
  .hero-text { color: var(--body); font-size: 12.5px; line-height: 19px; margin-top: 10px; width: 270px; }
  .cta { position: absolute; left: 237px; top: 385px; width: 202px; height: 41px; border-radius: 21px; background: var(--blue-deep); color: var(--white); font-size: 12.5px; font-weight: 500; display: flex; align-items: center; justify-content: center; gap: 7px; box-shadow: 0 8px 16px rgba(0,0,0,0.2); }

  .product-visual { position: absolute; left: 657px; top: 75px; width: 243px; height: 503px; background: linear-gradient(180deg, #e9ecef 0%, #7fa6d9 35%, #5d8fd2 65%, #eef0f2 100%); border: 6px solid #ffffff; }

  .features { position: absolute; top: 585px; left: 0; width: 1200px; }
  .feature { position: absolute; width: 200px; text-align: center; transform: translateX(-50%); }
  .feature-icon { height: 52px; display: flex; justify-content: center; align-items: center; }
  .feature-title { color: var(--blue-deep); font-size: 16.5px; font-weight: 700; margin-top: 18px; letter-spacing: 0.2px; }
  .feature-text { color: var(--body); font-size: 10px; line-height: 19px; margin-top: 3px; }
</style>
</head>
<body>
<div class="page">
  <svg class="backdrop" width="1200" height="771" viewBox="0 0 1200 771" aria-hidden="true">
    <defs>
      <linearGradient id="swoosh" x1="0" y1="0" x2="1" y2="1">
        <stop offset="0" stop-color="#0a4aa4"/>
        <stop offset="1" stop-color="#2e8ef2"/>
      </linearGradient>
      <linearGradient id="blob" x1="0" y1="0" x2="1" y2="1">
        <stop offset="0" stop-color="#1b64c9"/>
        <stop offset="1" stop-color="#2f92f4"/>
      </linearGradient>
    </defs>
    <path d="M538 0 H1200 V545 C1080 548 980 535 900 515 C790 460 700 310 640 200 C590 120 550 60 538 0 Z" fill="url(#swoosh)"/>
    <path d="M0 315 C130 330 230 430 235 590 C238 680 210 730 184 771 H0 Z" fill="url(#blob)"/>
  </svg>

  <div class="brand">
    <div class="brand-name">Corvenhall</div>
    <div class="brand-tag">Aluminium Windows &amp; Doors</div>
  </div>

  <nav class="nav">
    <a href="#">Home</a>
    <a href="#">Our Products</a>
    <a href="#">Why Corvenhall</a>
    <a href="#" class="enquiry">Make an Enquiry</a>
  </nav>

  <section class="hero-copy">
    <h1 class="hero-title">Bullet Resistant<br>Windows &amp; Doors</h1>
    <p class="hero-text">Lorem ipsum dolor sit amet, consectetur adipiscing elit, sed do eiusmod tempor incididunt ut labore et dolore magna aliqua.</p>
  </section>
  <a class="cta" href="#">Learn More
    <svg width="13" height="11" viewBox="0 0 13 11"><path d="M1 5.5 H11 M7 1.5 L11 5.5 L7 9.5" stroke="#fff" stroke-width="1.6" fill="none" stroke-linecap="round" stroke-linejoin="round"/></svg>
  </a>

  <div class="product-visual" role="img" aria-label="White aluminium sliding glass door with blue tinted bullet resistant panes"></div>

  <section class="features">
    <div class="feature" style="left:382px">
      <div class="feature-icon">
        <svg width="60" height="52" viewBox="0 0 60 52">
          <circle cx="18" cy="30" r="14" fill="#e6e6e6"/>
          <path d="M30 4 L48 11 V24 C48 36 40 44 30 49 C20 44 12 36 12 24 V11 Z" fill="none" stroke="#1a66cf" stroke-width="3"/>
          <path d="M30 6 V47 M13 24 H47" stroke="#1a66cf" stroke-width="3"/>
        </svg>
      </div>
      <div class="feature-title">Premium Protection</div>
      <p class="feature-text">Lorem ipsum dolor sit amet,<br>consectetur adipiscing elit,<br>sed do eiusmod.</p>
    </div>
    <div class="feature" style="left:610px">
      <div class="feature-icon">
        <svg width="66" height="54" viewBox="0 0 66 54">
          <circle cx="18" cy="34" r="14" fill="#e6e6e6"/>
          <path d="M8 2 L62 10 V46 L8 52 Z" fill="none" stroke="#1a66cf" stroke-width="2"/>
          <path d="M22 4 V50 M36 6 V49 M49 8 V47 M8 22 L62 24 M8 38 L62 37 M8 48 L62 43" stroke="#1a66cf" stroke-width="2" fill="none"/>
        </svg>
      </div>
      <div class="feature-title">Aesthetic Design</div>
      <p class="feature-text">Lorem ipsum dolor sit amet,<br>consectetur adipiscing elit,<br>sed do eiusmod.</p>
    </div>
    <div class="feature" style="left:839px">
      <div class="feature-icon">
        <svg width="66" height="52" viewBox="0 0 66 52">
          <circle cx="18" cy="30" r="14" fill="#e6e6e6"/>
          <rect x="13" y="6" width="30" height="38" rx="3" fill="none" stroke="#1a66cf" stroke-width="3"/>
          <path d="M24 6 V18 H33 V6" fill="none" stroke="#1a66cf" stroke-width="3"/>
          <path d="M49 14 H58 M46 24 H61 M49 34 H58" stroke="#2f90f2" stroke-width="3"/>
        </svg>
      </div>
      <div class="feature-title">Prompt Delivery</div>
      <p class="feature-text">Lorem ipsum dolor sit amet,<br>consectetur adipiscing elit,<br>sed do eiusmod.</p>
    </div>
  </section>
</div>
</body>
</html>
```